依頼概要
▽ターゲット
【■ 40~80歳■】向けの【■ ふとんの打ち直し■】販促用にポスターデザインを作成したいと考えており、デザイナー・クリエイターの方向けにコンペを開催いたします。

▽サイズ
【■A2サイズでトンボを付けて下さい。そのまま印刷屋に出せる形式(AIファイル必須■】

▽参考デザイン
サイト名:【■ ねむり堂川 ■】
参考URL:【■ http://www.nemuridokawa.co.jp/SHOP/582716/list.html■】

```html
<!DOCTYPE html>
<html lang="ja">
<head>
<meta charset="utf-8">
<title>ふとん仕立て直し承ります</title>
<link href="https://fonts.googleapis.com/css2?family=Mochiy+Pop+One&family=M+PLUS+Rounded+1c:wght@500;800;900&display=swap" rel="stylesheet">
<style>
  :root {
    --red: #e60012;
    --deep-red: #c4000f;
    --white: #ffffff;
    --yellow: #ffe600;
    --blue: #1d4fa8;
    --ink: #231815;
    --pink: #f6c9cf;
    --skin: #f7d9b8;
  }
  * { margin: 0; padding: 0; box-sizing: border-box; }
  html, body { width: 847px; height: 1200px; overflow: hidden; background: var(--white); }
  .poster {
    position: relative; width: 847px; height: 1200px;
    background: var(--red);
    font-family: "M PLUS Rounded 1c", sans-serif; color: var(--ink);
  }
  .poster-body {
    position: absolute; left: 12px; right: 12px; top: 140px; bottom: 64px;
    background: var(--white); border-radius: 10px;
  }
  .title-main {
    position: absolute; left: 26px; top: 6px;
    font-family: "Mochiy Pop One", sans-serif; font-size: 112px; line-height: 1.15;
    color: var(--white); letter-spacing: 2px;
  }
  .title-tag {
    position: absolute; left: 420px; top: 24px;
    background: var(--white); color: var(--red); border-radius: 12px;
    font-family: "Mochiy Pop One", sans-serif; font-size: 50px; line-height: 1; padding: 10px 18px;
  }
  .title-sub {
    position: absolute; left: 640px; top: 86px;
    font-family: "Mochiy Pop One", sans-serif; font-size: 40px; color: var(--white);
  }
  .headline {
    position: absolute; left: 300px; top: 150px; width: 540px;
    transform: rotate(-5deg); text-align: center;
    font-family: "Mochiy Pop One", sans-serif; color: var(--blue);
    -webkit-text-stroke: 0; text-shadow: 0 0 0 var(--yellow);
    paint-order: stroke fill;
  }
  .headline span { display: block; line-height: 1.2; -webkit-text-stroke: 8px var(--white); paint-order: stroke fill; }
  .headline .line-1 { font-size: 62px; }
  .headline .line-2 { font-size: 72px; color: var(--red); }
  .speech {
    position: absolute; left: 230px; top: 170px;
    font-family: "Mochiy Pop One", sans-serif; font-size: 26px; color: var(--red);
    transform: rotate(-8deg); line-height: 1.2; text-align: center;
  }
  .art { position: absolute; }
  .art-people { left: 40px; top: 165px; width: 190px; height: 190px; border-radius: 50% 50% 20px 20px;
    background: linear-gradient(180deg, var(--skin), #bcd8ee); }
  .art-futon-before { left: 50px; top: 330px; width: 340px; height: 180px; border-radius: 20px;
    background: linear-gradient(160deg, #fde3e6, var(--pink)); }
  .art-futon-after { left: 420px; top: 300px; width: 400px; height: 235px; border-radius: 36px;
    background: linear-gradient(160deg, #fff0f2, var(--pink)); }
  .before-after {
    position: absolute; left: 140px; top: 528px; width: 600px; display: flex; align-items: center; justify-content: center; gap: 18px;
    font-family: "Mochiy Pop One", sans-serif; font-size: 40px; color: var(--ink);
  }
  .before-after svg { width: 130px; height: 30px; }
  .campaign { position: absolute; left: 8px; top: 585px; width: 270px; height: 190px; }
  .campaign svg { position: absolute; inset: 0; }
  .campaign-text {
    position: absolute; inset: 0; display: flex; flex-direction: column; justify-content: center; align-items: center;
    font-family: "Mochiy Pop One", sans-serif; color: var(--red); font-size: 40px; line-height: 1.15;
    transform: rotate(-10deg);
  }
  .price-list { position: absolute; left: 300px; top: 590px; width: 520px; list-style: none; }
  .price-list li { display: flex; align-items: baseline; height: 56px; }
  .price-label { width: 230px; font-family: "Mochiy Pop One", sans-serif; font-size: 44px; color: var(--ink); }
  .price-value { font-family: "Mochiy Pop One", sans-serif; font-size: 50px; color: var(--red); }
  .price-note { position: absolute; right: 30px; top: 762px; font-size: 15px; font-weight: 500; }
  .detail-head {
    position: absolute; left: 28px; right: 28px; height: 36px; background: var(--red); color: var(--white);
    border-radius: 6px; font-size: 24px; font-weight: 800; line-height: 36px; padding-left: 14px;
  }
  .detail-list { position: absolute; left: 36px; right: 28px; list-style: none; font-size: 19px; font-weight: 800; line-height: 1.45; }
  .detail-list li::before { content: "●"; color: var(--red); margin-right: 4px; }
  .detail-list li.sub::before { content: ""; margin: 0; }
  .detail-list li.sub { padding-left: 24px; font-size: 17px; font-weight: 500; }
  .footer { position: absolute; left: 0; right: 0; bottom: 0; height: 64px; display: flex; align-items: center; justify-content: flex-end; gap: 18px; padding-right: 36px; color: var(--white); }
  .footer-tagline { font-size: 22px; font-weight: 800; }
  .footer-name { font-size: 42px; font-weight: 900; }
</style>
</head>
<body>
<div class="poster">
  <div class="title-main">ふとん</div>
  <div class="title-tag">仕立て直し</div>
  <div class="title-sub">承ります</div>

  <div class="poster-body"></div>

  <div class="art art-people" role="img" aria-label="寝具を喜ぶ夫婦のイラスト"></div>
  <div class="speech">ぐっすり<br>眠れるネ!</div>
  <div class="headline"><span class="line-1">新品同様に</span><span class="line-2">ふっくらに!!</span></div>
  <div class="art art-futon-before" role="img" aria-label="仕立て直し前の薄くなった花柄ふとん"></div>
  <div class="art art-futon-after" role="img" aria-label="仕立て直し後のふっくらした花柄ふとん"></div>

  <div class="before-after">
    <span>BEFORE</span>
    <svg viewBox="0 0 130 30" aria-hidden="true"><circle cx="10" cy="15" r="6" fill="#e60012"/><circle cx="34" cy="15" r="6" fill="#e60012"/><circle cx="58" cy="15" r="6" fill="#e60012"/><path d="M74 15h40M104 4l18 11-18 11" stroke="#e60012" stroke-width="7" fill="none" stroke-linejoin="round"/></svg>
    <span>AFTER</span>
  </div>

  <div class="campaign">
    <svg viewBox="0 0 270 190" aria-hidden="true"><polygon fill="#ffe600" points="135,2 155,35 195,12 198,50 245,40 228,78 268,95 228,112 245,150 198,140 195,178 155,155 135,188 115,155 75,178 72,140 25,150 42,112 2,95 42,78 25,40 72,50 75,12 115,35"/></svg>
    <div class="campaign-text"><span>キャンペーン</span><span>実施中!!</span></div>
  </div>

  <ul class="price-list">
    <li><span class="price-label">シングル</span><span class="price-value">¥3,800~</span></li>
    <li><span class="price-label">セミダブル</span><span class="price-value">¥9,800~</span></li>
    <li><span class="price-label">ダブル</span><span class="price-value">¥10,800~</span></li>
  </ul>
  <p class="price-note">表示価格は目安、敷き共に同じ価格です。</p>

  <h2 class="detail-head" style="top:800px">商品の詳細について</h2>
  <ul class="detail-list" style="top:842px">
    <li>商品のお布団は上記書くサイズより¥3,000UPでお送り致します。</li>
    <li>掛けの中綿は少し割高ですが米綿がおすすめです!</li>
    <li class="sub">(米綿の特徴は保温性、吸湿性の高さに加えしっとりと体にFITします)</li>
  </ul>

  <h2 class="detail-head" style="top:965px">仕立直し、新品共通の詳細について</h2>
  <ul class="detail-list" style="top:1007px">
    <li>柄は「おまかせ」で男柄か女柄かをご選択下さい。</li>
    <li>ロング丈(10cm長)は¥1,000UPで承ります。</li>
    <li class="sub">尚、枕やカバー等もご用意できます。 詳しくは店主まで</li>
  </ul>

  <footer class="footer">
    <span class="footer-tagline">クリーニングと寝具の店</span>
    <span class="footer-name">ふとんの東山</span>
  </footer>
</div>
</body>
</html>
```